Re-Design of a 1 Pager IT Security Website

Please create a 1 Pager design for this website and all its elements: http://www.vantorelgrid.com/

Colours, Fonts etc: You can select whatever you prefer

```html
<!DOCTYPE html>
<html lang="en">
<head>
<meta charset="utf-8">
<title>Domain Monitoring</title>
<link href="https://fonts.googleapis.com/css2?family=Poppins:wght@600;700;800&family=Roboto:wght@400;500;700&display=swap" rel="stylesheet">
<style>
:root{
  --navy:#0b0f4d;
  --navy-deep:#070a3a;
  --yellow:#d6c900;
  --yellow-bright:#e6d800;
  --ink:#111;
  --grey:#6b6b6b;
  --cream:#fbf8e7;
  --white:#fff;
  --tint-light:#eeeef3;
  --tint-navy:#1a1f5e;
  --tint-yellow:#e2d640;
}
*{box-sizing:border-box;margin:0;padding:0}
html,body{width:1200px;height:3525px;overflow:hidden}
body{font-family:'Roboto',sans-serif;color:var(--ink);background:var(--white);position:relative}
.btn{position:absolute;display:flex;align-items:center;justify-content:center;gap:10px;font:700 14px 'Roboto',sans-serif;text-transform:uppercase;border-radius:2px}
.btn-yellow{background:var(--yellow);color:var(--navy)}
.btn-navy{background:var(--navy);color:var(--yellow-bright)}
.btn svg{width:13px;height:13px}
.rule{position:absolute;width:36px;height:3px;background:var(--navy)}
.accent-block{position:absolute;background:var(--tint-light)}

/* hero */
.hero{position:absolute;left:0;top:0;width:1200px;height:612px;background:linear-gradient(100deg,#082a63 0%,#0b4ea0 45%,#0a2f6e 75%,#0a1838 100%);overflow:hidden}
.hero-art{position:absolute;left:600px;top:60px;width:380px;height:300px;border-radius:50%;background:radial-gradient(ellipse,rgba(120,210,255,.55),rgba(40,120,220,.15) 60%,transparent 75%)}
.logo{position:absolute;font:700 20px 'Poppins',sans-serif;color:var(--white);letter-spacing:.3px}
.nav{position:absolute;left:480px;top:31px;display:flex;gap:29px;font:700 13.5px 'Roboto',sans-serif;color:var(--white)}
.nav .active{color:var(--yellow-bright)}
.socials{position:absolute;display:flex;gap:7px}
.socials span{width:30px;height:30px;border-radius:50%;background:var(--yellow)}
.hero h1{position:absolute;left:111px;top:215px;width:520px;font:800 45px/52px 'Poppins',sans-serif;color:var(--white)}
.hero p{position:absolute;left:113px;top:388px;width:470px;font:700 14px/25px 'Roboto',sans-serif;color:var(--white)}

/* risk */
.section-title{position:absolute;left:0;width:1200px;text-align:center;font:700 29px 'Poppins',sans-serif}
.center-text{position:absolute;left:111px;width:978px;text-align:justify;text-align-last:center;font:400 14.5px/26px 'Roboto',sans-serif;color:var(--grey)}
.attack-card{position:absolute;top:899px;width:316px;height:235px;display:flex;flex-direction:column;align-items:center;justify-content:flex-end;padding-bottom:32px;color:var(--white);font:700 20px 'Roboto',sans-serif}
.attack-card svg{width:44px;height:44px;margin-bottom:8px}
.bar{position:absolute;width:230px;background:var(--yellow)}

/* about */
.about{position:absolute;left:0;top:1249px;width:1200px;height:526px;background:var(--navy)}
.about .accent-block{background:var(--tint-navy)}
.photo{position:absolute;border-radius:16px}
.play{position:absolute;width:30px;height:30px;border-radius:50%;background:var(--yellow)}
.about h2{position:absolute;left:610px;top:92px;font:700 30px 'Poppins',sans-serif;color:var(--white)}
.about .rule{background:var(--white);left:610px;top:146px}
.about p{position:absolute;left:610px;top:175px;width:477px;font:700 14px/30px 'Roboto',sans-serif;color:var(--white);text-align:justify}

/* monitoring */
.monitor-title{position:absolute;left:111px;top:1915px;font:700 25px 'Poppins',sans-serif}
.monitor-text{position:absolute;left:111px;top:1987px;width:472px;font:400 14.5px/25.8px 'Roboto',sans-serif;color:var(--grey);text-align:justify}
.service{position:absolute;width:188px;height:200px;background:var(--white);border:1px solid #e2e2e2;box-shadow:0 4px 14px rgba(0,0,0,.05);display:flex;flex-direction:column;align-items:center;padding-top:16px;text-align:center}
.service svg{width:52px;height:52px}
.service h3{font:500 16.5px/21px 'Roboto',sans-serif;color:var(--ink);margin-top:12px}
.service .line{width:26px;height:2px;background:var(--yellow);margin:10px 0 9px}
.service p{font:400 12.5px/18px 'Roboto',sans-serif;color:var(--grey)}
.service.dark{background:var(--navy);border-color:var(--navy)}
.service.dark h3,.service.dark p{color:var(--white)}

/* cta */
.cta{position:absolute;left:0;top:2383px;width:1200px;height:394px;background:var(--yellow)}
.cta .accent-block{background:var(--tint-yellow)}
.cta .center-text{color:var(--navy-deep)}

/* contact */
.contact{position:absolute;left:0;top:2777px;width:1200px;height:520px;background:var(--cream);overflow:hidden}
.contact .accent-block{background:#f1edd6}
.contact-bg{position:absolute;left:440px;top:0;width:760px;height:520px;background:radial-gradient(ellipse at 60% 40%,rgba(210,200,150,.35),transparent 70%)}
.contact h2{position:absolute;font:700 29px 'Poppins',sans-serif}
.info{position:absolute;left:111px;display:flex;gap:18px}
.info svg{width:28px;height:28px;margin-top:4px}
.info b{display:block;font:700 13px 'Roboto',sans-serif;margin-bottom:6px}
.info span{font:400 13px 'Roboto',sans-serif}
.divider{position:absolute;left:477px;top:89px;width:2px;height:342px;background:#d9d6c4}
.field{position:absolute;height:45px;background:var(--white);border:1px solid #e8e1a6;display:flex;align-items:center;justify-content:space-between;padding:0 16px;font:400 14px 'Roboto',sans-serif;color:#7a7a7a}
.field svg{width:14px;height:14px}
.field.message{align-items:flex-start;padding-top:14px;height:93px}

/* footer */
.footer{position:absolute;left:0;top:3297px;width:1200px;height:228px;background:var(--navy-deep)}
.footer-nav{position:absolute;left:547px;top:68px;display:flex;gap:20px;font:700 13.5px 'Roboto',sans-serif;color:var(--white)}
.footer-line{position:absolute;left:547px;top:109px;width:540px;height:1px;background:#2b2f6e}
.copy{position:absolute;right:113px;top:146px;font:400 14px 'Roboto',sans-serif;color:var(--white)}
</style>
</head>
<body>

<section class="hero">
  <div class="hero-art" role="img" aria-label="Glowing digital padlock and security icons above an outstretched hand"></div>
  <div class="logo" style="left:112px;top:24px">DOMAIN MONITORING</div>
  <nav class="nav"><span class="active">Home</span><span>About</span><span>What Is Risk</span><span>How to Protect</span><span>Contact</span></nav>
  <div class="socials" style="left:946px;top:25px" aria-label="Social links"><span></span><span></span><span></span><span></span></div>
  <h1>Prevent Attacks By Monitoring Your Domains</h1>
  <p>Hackers use domain-based attacks, which are designed to trick users into submitting sensitive data or downloading dangerous files.</p>
  <div class="btn btn-yellow" style="left:114px;top:461px;width:151px;height:46px">Get Started
    <svg viewBox="0 0 16 16"><circle cx="8" cy="8" r="8" fill="#0b0f4d"/><path d="M6.5 4.5 10 8l-3.5 3.5" stroke="#d6c900" stroke-width="2" fill="none"/></svg></div>
</section>

<h2 class="section-title" style="top:682px">WHAT IS THE RISK ?</h2>
<div class="rule" style="left:582px;top:733px"></div>
<p class="center-text" style="top:757px">Hackers use domain-based attacks, which are designed to trick users into submitting sensitive data or downloading dangerous files. This is often the case with phishing attacks. For example, domains can be registered that are very similar to one's own company, a customer or a supplier. Once a fraudulent domain is registered, the hackers try to lure the employee to the website. This can be done via e-mail, SMS (smishing), instant messaging. Social media and many other techniques succeed. A distinction is made between different types of attacks:</p>

<div class="bar" style="left:152px;top:891px;height:8px"></div>
<div class="bar" style="left:485px;top:891px;height:8px"></div>
<div class="bar" style="left:818px;top:891px;height:8px"></div>
<div class="bar" style="left:152px;top:1134px;height:19px"></div>
<div class="bar" style="left:485px;top:1134px;height:19px"></div>
<div class="bar" style="left:818px;top:1134px;height:19px"></div>

<div class="attack-card" style="left:109px;background:linear-gradient(160deg,#d8c9b4,#8a7a6a)" role="img" aria-label="Person typing a search on a laptop">
  <svg viewBox="0 0 44 44" fill="none" stroke="#fff" stroke-width="2"><circle cx="22" cy="22" r="18"/><ellipse cx="22" cy="22" rx="8" ry="18"/><path d="M4 22h36"/></svg>Domain Spoofing</div>
<div class="attack-card" style="left:442px;background:linear-gradient(160deg,#4a86b8,#12315a)" role="img" aria-label="Magnifying glass over a domain symbol on a blue code screen">
  <svg viewBox="0 0 44 44" fill="#fff"><rect x="4" y="8" width="22" height="10" rx="2"/><rect x="4" y="22" width="22" height="10" rx="2"/><circle cx="33" cy="30" r="7" fill="none" stroke="#fff" stroke-width="3"/></svg>Homoglyphic Attack</div>
<div class="attack-card" style="left:775px;background:linear-gradient(160deg,#a8a4b8,#4c4a60)" role="img" aria-label="Hands typing on a laptop keyboard">
  <svg viewBox="0 0 44 44" fill="none" stroke="#fff" stroke-width="2.5"><rect x="6" y="6" width="32" height="32" stroke-dasharray="4 3"/><path d="M14 14h16M22 14v18"/></svg>Typosquatting</div>

<section class="about">
  <div class="accent-block" style="left:87px;top:85px;width:88px;height:60px" role="img" aria-label="Decorative dot pattern"></div>
  <div class="accent-block" style="left:465px;top:380px;width:86px;height:70px" role="img" aria-label="Decorative dot pattern"></div>
  <div class="photo" style="left:112px;top:108px;width:323px;height:252px;background:linear-gradient(135deg,#b89a6a,#3a4a4a)" role="img" aria-label="Two colleagues reviewing data on computer monitors"></div>
  <div class="photo" style="left:291px;top:243px;width:230px;height:178px;background:linear-gradient(135deg,#8a7060,#2c2a30);border:2px solid var(--navy)" role="img" aria-label="Developer working at a desk with code on screens"></div>
  <div class="play" style="left:392px;top:318px"></div>
  <h2>ABOUT VELTRIX</h2>
  <div class="rule"></div>
  <p>Veltrix (company registration number CHE-418.206.957) was started in 2018 as a public limited company in Zug, Switzerland. Our analysts have long-standing relationships with various players on the Darknet. These personal relationships make it possible for Veltrix to repeatedly obtain the latest data leaks. Those unique data leaks are published by the press around the world.</p>
  <div class="btn btn-yellow" style="left:610px;top:379px;width:151px;height:46px">Learn More
    <svg viewBox="0 0 16 16"><circle cx="8" cy="8" r="8" fill="#0b0f4d"/><path d="M6.5 4.5 10 8l-3.5 3.5" stroke="#d6c900" stroke-width="2" fill="none"/></svg></div>
</section>

<div class="accent-block" style="left:0;top:1835px;width:88px;height:62px" role="img" aria-label="Decorative dot pattern"></div>
<div class="accent-block" style="left:1000px;top:2050px;width:88px;height:62px" role="img" aria-label="Decorative dot pattern"></div>
<div class="accent-block" style="left:630px;top:2226px;width:88px;height:62px" role="img" aria-label="Decorative dot pattern"></div>
<h2 class="monitor-title">WHAT ELSE ARE WE MONITORING?</h2>
<div class="rule" style="left:111px;top:1963px"></div>
<p class="monitor-text">Veltrix helps you understand when, where and how stolen or accidentally leaked information in dark web markets, forums, botnet logs, IRC, social media and other sources is exposed. Veltrix's alerting service can also detect threats before they turn into incidents. Veltrix offers AI-driven dark web analysis, real-time threat alerts and pre-Attack threat indicators. Setup in minutes you will receive instant access to real-time reporting including</p>
<div class="btn btn-yellow" style="left:111px;top:2175px;width:151px;height:46px">Learn More
  <svg viewBox="0 0 16 16"><circle cx="8" cy="8" r="8" fill="#0b0f4d"/><path d="M6.5 4.5 10 8l-3.5 3.5" stroke="#d6c900" stroke-width="2" fill="none"/></svg></div>

<div class="service" style="left:661px;top:1848px">
  <svg viewBox="0 0 52 52" fill="#0b0f4d"><circle cx="26" cy="26" r="11" fill="none" stroke="#0b0f4d" stroke-width="3"/><path d="M26 15a11 11 0 0 1 0 22z"/><g stroke="#0b0f4d" stroke-width="3"><path d="M26 2v7M26 43v7M2 26h7M43 26h7M9 9l5 5M38 38l5 5M9 43l5-5M38 14l5-5"/></g></svg>
  <h3>Infrastructure<br>Exposure</h3><div class="line"></div><p>IOT, Git, Cloud, Repos<br>&amp; more</p></div>
<div class="service" style="left:866px;top:1877px">
  <svg viewBox="0 0 52 52" fill="#0b0f4d"><circle cx="14" cy="16" r="6"/><circle cx="38" cy="16" r="6"/><circle cx="26" cy="18" r="8"/><path d="M2 38c0-8 5-12 12-12s10 4 10 4H2zM50 38c0-8-5-12-12-12s-10 4-10 4h22z"/><path d="M12 46c0-10 6-16 14-16s14 6 14 16z"/></svg>
  <h3>People<br>Exposure</h3><div class="line"></div><p>Social Media<br>Monitoring</p></div>
<div class="service dark" style="left:661px;top:2067px">
  <svg viewBox="0 0 52 52" fill="none" stroke="#fff" stroke-width="3"><rect x="5" y="6" width="42" height="30"/><path d="M18 46h16M26 36v10"/><rect x="20" y="19" width="12" height="10" fill="#fff"/><path d="M22 19v-4a4 4 0 0 1 8 0v4"/></svg>
  <h3>Ransomware<br>Exposure</h3><div class="line"></div><p>Leak &amp; Credential<br>Monitoring</p></div>
<div class="service" style="left:866px;top:2097px">
  <svg viewBox="0 0 52 52" fill="none" stroke="#0b0f4d" stroke-width="3"><circle cx="26" cy="26" r="14"/><circle cx="21" cy="23" r="3" fill="#0b0f4d"/><circle cx="31" cy="23" r="3" fill="#0b0f4d"/><path d="M20 32h12M26 2v8M26 42v8M2 26h8M42 26h8M9 9l6 6M37 37l6 6M9 43l6-6M37 15l6-6"/></svg>
  <h3>Attack<br>Prevention</h3><div class="line"></div><p>Domain and Certificate<br>Monitoring</p></div>

<section class="cta">
  <div class="accent-block" style="left:0;top:0;width:88px;height:62px" role="img" aria-label="Decorative dot pattern"></div>
  <div class="accent-block" style="left:1112px;top:330px;width:88px;height:62px" role="img" aria-label="Decorative dot pattern"></div>
  <h2 class="section-title" style="top:70px;color:var(--navy-deep)">WHAT IS THE RISK ?</h2>
  <div class="rule" style="left:582px;top:121px;background:var(--navy-deep)"></div>
  <p class="center-text" style="top:146px">Hackers use domain-based attacks, which are designed to trick users into submitting sensitive data or downloading dangerous files. This is often the case with phishing attacks. For example, domains can be registered that are very similar to one's own company, a customer or a supplier. Once a fraudulent domain is registered, the hackers try to lure the employee to the website. This can be done via e-mail, SMS (smishing), instant messaging. Social media and many other techniques succeed. A distinction is made between different types of attacks:</p>
  <div class="btn btn-navy" style="left:524px;top:275px;width:151px;height:47px">Learn More
    <svg viewBox="0 0 16 16"><circle cx="8" cy="8" r="8" fill="#e6d800"/><path d="M6.5 4.5 10 8l-3.5 3.5" stroke="#0b0f4d" stroke-width="2" fill="none"/></svg></div>
</section>

<section class="contact">
  <div class="contact-bg" role="img" aria-label="Faint hooded figure over a city skyline"></div>
  <div class="accent-block" style="left:343px;top:0;width:88px;height:62px" role="img" aria-label="Decorative dot pattern"></div>
  <div class="accent-block" style="left:0;top:460px;width:88px;height:60px" role="img" aria-label="Decorative dot pattern"></div>
  <h2 style="left:110px;top:88px">CONTACT US</h2>
  <div class="info" style="top:159px">
    <svg viewBox="0 0 28 28" fill="none" stroke="#111" stroke-width="1.6"><path d="M14 26s-9-9-9-15a9 9 0 0 1 18 0c0 6-9 15-9 15z"/><circle cx="14" cy="11" r="3.5"/></svg>
    <div><b>ADDRESS :</b><span>175 , Lorem Ipsum Dolor , United States</span></div></div>
  <div class="info" style="top:229px">
    <svg viewBox="0 0 28 28" fill="none" stroke="#111" stroke-width="1.6"><rect x="2" y="6" width="24" height="16"/><path d="M2 6l12 9 12-9M2 22l9-8M26 22l-9-8"/></svg>
    <div><b>EMAIL US :</b><span>info@vantorelgrid.com</span></div></div>
  <div class="info" style="top:298px">
    <svg viewBox="0 0 28 28" fill="none" stroke="#111" stroke-width="1.6"><path d="M6 3l5 5-3 3c1 3 5 7 8 8l3-3 5 5-4 4C11 25 3 17 2 7z"/><path d="M17 4a8 8 0 0 1 7 7M17 8a4 4 0 0 1 3 3"/></svg>
    <div><b>CALL US :</b><span>+ 1 555 014 2873 , + 1 555 019 6420</span></div></div>
  <div class="divider"></div>
  <h2 style="left:564px;top:88px">GET IN TOUCH</h2>
  <div class="field" style="left:565px;top:144px;width:256px">First Name<svg viewBox="0 0 14 14" fill="#777"><circle cx="7" cy="4" r="3"/><path d="M1 14c0-4 3-6 6-6s6 2 6 6z"/></svg></div>
  <div class="field" style="left:832px;top:144px;width:256px">Last Name<svg viewBox="0 0 14 14" fill="#777"><circle cx="7" cy="4" r="3"/><path d="M1 14c0-4 3-6 6-6s6 2 6 6z"/></svg></div>
  <div class="field" style="left:565px;top:203px;width:256px">Email Address<svg viewBox="0 0 14 14" fill="#777"><rect x="0" y="3" width="14" height="9"/><path d="M0 3l7 5 7-5" stroke="#fff" fill="none"/></svg></div>
  <div class="field" style="left:832px;top:203px;width:256px">Phone No<svg viewBox="0 0 14 14" fill="#777"><path d="M3 1l3 3-2 2c1 2 2 3 4 4l2-2 3 3-2 2C5 13 1 9 1 3z"/></svg></div>
  <div class="field message" style="left:565px;top:264px;width:523px">Message<svg viewBox="0 0 14 14" fill="none" stroke="#777" stroke-width="1.3"><path d="M1 2h9v6H5l-3 2V8H1z"/><path d="M10 5h3v5h-1v2l-2-2H6V8"/></svg></div>
  <div class="btn btn-navy" style="left:565px;top:375px;width:144px;height:44px">Submit Now
    <svg viewBox="0 0 16 16"><circle cx="8" cy="8" r="8" fill="#e6d800"/><path d="M6.5 4.5 10 8l-3.5 3.5" stroke="#0b0f4d" stroke-width="2" fill="none"/></svg></div>
</section>

<footer class="footer">
  <div class="logo" style="left:111px;top:85px;font-size:30px">DOMAIN MONITORING</div>
  <nav class="footer-nav"><span>HOME</span><span>|</span><span>ABOUT US</span><span>|</span><span>WHAT IS RISK</span><span>|</span><span>TEAM</span><span>|</span><span>CONTACT</span></nav>
  <div class="footer-line"></div>
  <div class="socials" style="left:540px;top:137px;gap:13px" aria-label="Social links"><span></span><span></span><span></span></div>
  <div class="copy">© 2022 Domain Monitoring. All Rights Reserved</div>
</footer>

</body>
</html>
```